Brin-well Tide Port Custom Brokers Limited

Name: Loranda Pascoe
Title: Customs Broker
Address: Shop 9 Fernvale Commercial Complex
227-229 Marrow Lane
Kingston 8
Telephone: (876)
Email: tideportbrin@quillmail.example

```html
<!DOCTYPE html>
<html lang="en">
<head>
<meta charset="utf-8">
<title>Brin-well Tide Port Custom Brokers Limited – Business Card</title>
<link rel="stylesheet" href="https://fonts.googleapis.com/css2?family=Montserrat:wght@400;500;600&display=swap">
<style>
  :root {
    --navy: #0b2a4d;
    --gold: #e3a51f;
    --paper: #f7f8f7;
    --ink-soft: #9aa2ab;
    --backdrop: #e7e7e7;
    --globe-light: rgba(160, 168, 176, 0.28);
    --globe-dark: rgba(255, 255, 255, 0.10);
  }
  * { box-sizing: border-box; margin: 0; padding: 0; }
  html, body {
    width: 1200px; height: 906px; overflow: hidden;
    background: var(--backdrop);
    font-family: "Montserrat", Arial, sans-serif;
  }
  .canvas {
    position: relative; width: 1200px; height: 906px;
  }
  .card {
    position: absolute; top: 283px;
    width: 540px; height: 340px;
    border-radius: 22px; overflow: hidden;
    box-shadow: 0 10px 28px rgba(0, 0, 0, 0.16);
  }
  .card--front { left: 40px; background: var(--paper); }
  .card--back  { left: 620px; background: var(--navy); }

  .globe-art {
    position: absolute; border-radius: 50%;
  }
  .card--front .globe-art {
    width: 360px; height: 360px; right: -70px; bottom: -120px;
    background: radial-gradient(circle, var(--globe-light) 0%, rgba(160,168,176,0.08) 70%, transparent 71%);
  }
  .card--back .globe-art {
    width: 420px; height: 420px; right: -110px; top: -40px;
    background: radial-gradient(circle, var(--globe-dark) 0%, rgba(255,255,255,0.03) 70%, transparent 71%);
  }

  .brand {
    position: absolute; display: flex; align-items: center; gap: 10px;
    font-weight: 600; letter-spacing: 0.04em; text-transform: uppercase;
  }
  .brand__dot {
    width: 14px; height: 14px; border-radius: 50%; background: var(--gold); flex: none;
  }
  .card--front .brand {
    left: 34px; top: 30px; color: var(--navy); font-size: 15px; line-height: 1.25;
  }
  .card--back .brand {
    left: 0; right: 0; top: 142px; justify-content: center;
    color: #ffffff; font-size: 24px; line-height: 1.2; text-align: center;
  }

  .person {
    position: absolute; left: 34px; top: 118px;
  }
  .person__name {
    color: var(--navy); font-weight: 600; font-size: 25px; letter-spacing: 0.02em;
    text-transform: uppercase;
  }
  .person__title {
    color: var(--gold); font-weight: 500; font-size: 19px; margin-top: 2px;
  }
  .contacts { list-style: none; margin-top: 10px; }
  .contacts li {
    display: flex; align-items: center; gap: 10px;
    color: var(--navy); font-size: 14px; font-weight: 500; margin-bottom: 6px;
  }
  .contacts svg { width: 18px; height: 18px; flex: none; }
  .address {
    margin-top: 14px; font-style: normal;
    color: var(--navy); font-size: 15px; font-weight: 500; line-height: 1.35;
  }
</style>
</head>
<body>
<main class="canvas">

  <section class="card card--front" aria-label="Business card front">
    <div class="globe-art" role="img" aria-label="Faint wireframe globe decoration"></div>

    <div class="brand">
      <span class="brand__dot"></span>
      <span>Brin-well Tide Port<br>Custom Brokers Ltd.</span>
    </div>

    <div class="person">
      <h1 class="person__name">Loranda Pascoe</h1>
      <p class="person__title">Customs Broker</p>
      <ul class="contacts">
        <li>
          <svg viewBox="0 0 20 20" aria-hidden="true">
            <circle cx="10" cy="10" r="9" fill="var(--gold)"/>
            <path d="M7 5.5l1.6 2.6-1 1.1a6 6 0 0 0 3.2 3.2l1.1-1 2.6 1.6-.8 1.6c-3.8 0-7.8-4-7.8-7.8z" fill="#fff"/>
          </svg>
          <span>(876)</span>
        </li>
        <li>
          <svg viewBox="0 0 20 20" aria-hidden="true">
            <rect x="1.5" y="4" width="17" height="12" rx="1.5" fill="var(--gold)"/>
            <path d="M2.5 5l7.5 6 7.5-6" fill="none" stroke="#fff" stroke-width="1.4"/>
          </svg>
          <span>tideportbrin@quillmail.example</span>
        </li>
      </ul>
      <address class="address">
        Shop 9 Fernvale Commercial Complex<br>
        227-229 Marrow Lane, Kingston 8
      </address>
    </div>
  </section>

  <section class="card card--back" aria-label="Business card back">
    <div class="globe-art" role="img" aria-label="Faint wireframe globe decoration"></div>
    <div class="brand">
      <span class="brand__dot"></span>
      <span>Brin-well Tide Port</span>
    </div>
  </section>

</main>
</body>
</html>
```